New Wedding Decor Web Design Project - GUARANTEED PAYMENT

We need to have a business website for a brand new wedding decor & events company, Lirovelle. We have just established our logo and would love to use this logo on the website.

Because this is a new business venture, we do not have too many pictures to post online. It'd be exciting what your creativity can bring us!

Our website is: www.Lirovelle.ca

Target Market(s)

Our clientele demographic is targeted to brides and bridesmaids in their 20-30 years old.

Industry/Entity Type

Wedding

Requirements
Must have
• - Professional, elegant and artistic look
- Modern feeling
- Very catchy flash intro page
- Ability to show Chatterbook posts
Nice to have
• - Easy to navigate, crisp and clean
- Live vocaline messaging or online messaging

I would like to have navigation pages like: Lirovelle Brand, Collections, Features, Contact Us, etc.

Each page I want it to be clean and easy to read. Something like the following website: http://www.pardunetho.com/

We offer:
BACKDROPS
HEAD, CAKE & RECEIVING TABLES DECOR
CHAIRCOVERS
TABLE CLOTHS & OVERLAYS
NAPKINS
CENTREPIECES
CEREMONY SET-UP
CANDELABRA
CRYSTAL GLOBES
LED LIGHTING
CUSTOM DESIGN AISLE RUNNERS
CAKE STANDS
MONEY BOX
CHARGERS
GOBO LIGHTING
Should not have
• - traditional, old style website
- very static (dull)
- too many images or busy layout
- no "standardized" website templates such as: www.brintaq.com/gallery/weddings

```html
<!DOCTYPE html>
<html lang="en">
<head>
<meta charset="utf-8">
<title>Lirovelle — Features</title>
<link rel="stylesheet" href="https://fonts.googleapis.com/css2?family=Quicksand:wght@400;500&family=Arimo:wght@400&display=swap">
<style>
  :root{
    --page-grey:#d8d8d8;
    --stage-grey:#dcdcdc;
    --panel-fill:#ececec;
    --panel-edge:#ffffff;
    --plum-deep:#2a0b3a;
    --plum-mid:#5a3a6e;
    --plum-glow:#7e6390;
    --accent-pink:#e4107a;
    --ink:#3f3f3f;
    --caption-ink:#444;
    --white:#ffffff;
    --social:#a892b5;
    --badge-blue:#27b4ea;
    --badge-green:#6cc43a;
  }
  *{box-sizing:border-box;margin:0;padding:0}
  html,body{width:1200px;height:897px;overflow:hidden}
  body{position:relative;background:var(--page-grey);font-family:"Arimo",Arial,sans-serif;color:var(--ink)}

  .site-header{position:absolute;left:0;top:42px;width:1200px;height:145px;
    background:radial-gradient(ellipse 420px 200px at 600px 70px,var(--plum-glow),var(--plum-mid) 45%,var(--plum-deep) 100%)}
  .main-nav a{position:absolute;top:79px;color:var(--white);text-decoration:none;font-size:15px;letter-spacing:.2px;transform:translateX(-50%);white-space:nowrap}
  .nav-active{position:absolute;left:946px;top:136px;width:142px;height:9px;background:var(--accent-pink)}

  .brand-shield{position:absolute;left:476px;top:0;width:249px;height:178px}
  .brand-mark{position:absolute;left:515px;top:62px;display:flex;align-items:center;gap:8px;font-family:"Quicksand",sans-serif;font-size:30px;font-weight:500;color:#555}
  .brand-mark .dot{width:16px;height:16px;border-radius:50%;background:var(--accent-pink)}

  .online-badge{position:absolute;left:922px;top:47px;width:152px;height:36px}
  .online-badge .pill{position:absolute;left:8px;top:9px;width:143px;height:25px;border-radius:4px;background:linear-gradient(#7ed6f7,var(--badge-blue));border:1px solid #1c8fc0}
  .online-badge .pill span{position:absolute;left:0;right:0;top:4px;text-align:center;color:var(--white);font-size:13px}
  .online-badge .tick{position:absolute;left:0;top:0;width:32px;height:32px}

  .stage{position:absolute;left:0;top:187px;width:1200px;height:576px;background:var(--stage-grey)}
  .panel{position:absolute;left:111px;top:203px;width:973px;height:533px;background:var(--panel-fill);border:5px solid var(--panel-edge);border-radius:4px}

  .section-title{position:absolute;left:132px;top:236px;width:203px;height:42px;border:1px solid #bbb;border-bottom:none}
  .section-title h1{position:absolute;left:30px;top:20px;padding:0 6px;background:var(--panel-fill);font-family:"Quicksand",sans-serif;font-weight:400;font-size:30px;color:#444;line-height:1}
  .title-flower{position:absolute;left:205px;top:215px;width:50px;height:40px;border-radius:50%;background:radial-gradient(#f47ab4,#d91a73);}

  .slide{position:absolute;background:var(--white);padding:6px;border-radius:4px;box-shadow:0 10px 10px -6px rgba(0,0,0,.45)}
  .slide .photo{width:100%;height:100%}
  .slide-caption{position:absolute;font-family:"Quicksand",sans-serif;color:var(--caption-ink);transform:translateX(-50%);white-space:nowrap}

  .arrow{position:absolute;width:42px;height:41px;border-radius:5px;background:linear-gradient(#f6f6f6,#bdbdbd);box-shadow:0 1px 2px rgba(0,0,0,.4)}
  .arrow svg{position:absolute;left:5px;top:8px}

  .site-footer{position:absolute;left:0;top:763px;width:1200px;height:134px;
    background:radial-gradient(ellipse 420px 180px at 600px 60px,var(--plum-glow),var(--plum-mid) 45%,var(--plum-deep) 100%)}
  .footer-brand{position:absolute;left:118px;top:58px;display:flex;align-items:center;gap:8px;font-family:"Quicksand",sans-serif;font-size:32px;font-weight:500;color:#8a8a8a}
  .footer-brand .dot{width:16px;height:16px;border-radius:50%;background:#8a8a8a}
  .footer-links{position:absolute;left:0;width:1200px;top:53px;text-align:center;font-size:12.5px;color:var(--white)}
  .footer-links a{color:var(--white);text-decoration:none}
  .footer-links .sep{margin:0 13px}
  .copyright{position:absolute;left:0;width:1200px;top:79px;text-align:center;font-size:12.5px;color:var(--white)}
  .social{position:absolute;top:59px;width:27px;height:27px;border-radius:50%;background:var(--social)}
</style>
</head>
<body>

<header class="site-header">
  <nav class="main-nav">
    <a href="#" style="left:191px">LIROVELLE BRAND</a>
    <a href="#" style="left:389px">COLLECTIONS</a>
    <a href="#" style="left:820px">FEATURES</a>
    <a href="#" style="left:1013px">CONTACT US</a>
  </nav>
  <div class="nav-active"></div>
</header>

<svg class="brand-shield" viewBox="0 0 249 178">
  <defs><linearGradient id="shieldFill" x1="0" y1="0" x2="0" y2="1"><stop offset="0" stop-color="#fff"/><stop offset="1" stop-color="#e2e2e2"/></linearGradient></defs>
  <path d="M0 0H249V96L124.5 176L0 96Z" fill="url(#shieldFill)" stroke="#b9a9c4"/>
</svg>
<div class="brand-mark"><span class="dot"></span>Lirovelle</div>

<div class="online-badge">
  <div class="pill"><span>I'm online</span></div>
  <svg class="tick" viewBox="0 0 32 32"><circle cx="16" cy="16" r="15" fill="var(--badge-green)" stroke="#fff" stroke-width="2"/><path d="M9 16l5 5 9-10" fill="none" stroke="#fff" stroke-width="3.5" stroke-linecap="round"/></svg>
</div>

<main>
  <div class="stage"></div>
  <section class="panel"></section>

  <div class="section-title"><h1>Features</h1></div>
  <div class="title-flower" role="img" aria-label="Pink peony flower ornament"></div>

  <div class="slide" style="left:140px;top:430px;width:110px;height:115px"><div class="photo" role="img" aria-label="Chairs with pink covers and sashes" style="background:linear-gradient(#f0a9c8,#d77fa8)"></div></div>
  <div class="slide-caption" style="left:193px;top:552px;font-size:13px">Mauris vel</div>

  <div class="slide" style="left:216px;top:404px;width:150px;height:159px"><div class="photo" role="img" aria-label="Red and gold ceremony stage decor" style="background:linear-gradient(#e2b46a,#b9502a 60%,#c23a2a)"></div></div>
  <div class="slide-caption" style="left:300px;top:575px;font-size:13px">Curabitur</div>

  <div class="slide" style="left:944px;top:430px;width:109px;height:115px"><div class="photo" role="img" aria-label="Reception room with pink table linens" style="background:linear-gradient(#f4e7df,#e8b3be)"></div></div>
  <div class="slide-caption" style="left:993px;top:552px;font-size:13px">Mauris vel</div>

  <div class="slide" style="left:798px;top:404px;width:150px;height:159px"><div class="photo" role="img" aria-label="Chairs with grey satin covers" style="background:linear-gradient(90deg,#6f6675,#b7aeb9 50%,#e7d9c7)"></div></div>
  <div class="slide-caption" style="left:870px;top:575px;font-size:13px">Curabitur</div>

  <div class="slide" style="left:330px;top:334px;width:507px;height:285px"><div class="photo" role="img" aria-label="Head table with white draped backdrop under purple lighting" style="background:linear-gradient(160deg,#d9b6f3,#a66ad6 45%,#7d3aa8 75%,#5a2468)"></div></div>
  <div class="slide-caption" style="left:592px;top:627px;font-size:18px">Fusce ultricies</div>

  <a class="arrow" href="#" style="left:80px;top:456px" aria-label="Previous"><svg width="32" height="26" viewBox="0 0 32 26"><path d="M2 13L14 2V8H30V18H14V24Z" fill="#4a4a4a"/></svg></a>
  <a class="arrow" href="#" style="left:1064px;top:477px" aria-label="Next"><svg width="32" height="26" viewBox="0 0 32 26"><path d="M30 13L18 2V8H2V18H18V24Z" fill="#333"/></svg></a>
</main>

<footer class="site-footer">
  <div class="footer-brand"><span class="dot"></span>Lirovelle</div>
  <div class="footer-links">
    <a href="#">Lirovelle Brand</a><span class="sep">|</span><a href="#">Collections</a><span class="sep">|</span><a href="#">Features</a><span class="sep">|</span><a href="#">Contact Us</a>
  </div>
  <p class="copyright">Copyright © BrightHollow.com 2012, All Rights Reserved</p>
  <span class="social" style="left:894px"></span>
  <span class="social" style="left:932px"></span>
  <span class="social" style="left:970px"></span>
  <span class="social" style="left:1008px"></span>
  <svg class="social" style="left:1046px" viewBox="0 0 27 27" aria-label="Email"><circle cx="13.5" cy="13.5" r="13.5" fill="var(--social)"/><rect x="7" y="9" width="13" height="9" rx="1" fill="none" stroke="#2a0b3a" stroke-width="1.5"/><path d="M7 9l6.5 5 6.5-5" fill="none" stroke="#2a0b3a" stroke-width="1.5"/></svg>
</footer>

</body>
</html>
```